Brolga Ridge Earthmoving & Transport Business Card

Can you please design a business card for an Earthworks, Haulage truck and machinery hire company. They also provide sand soil and mulch supply, as well as screening of products. Can you re-create the logo from the attached but add Brolga Ridge Earthmoving & Transport just use the three diamond design.

Target Market(s)

Earthmoving and Transport, Landscapers, Construction

Contact Information for Business Card

ABN 52 907 338 214, Dale Pettigrew, Managing Director, Brolga Ridge Earthmoving & Transport Mobile 0438 256 904 Email brgtransport2011@haulmail.example

Font styles to use
Sans Serif

Colors
ec1f27
000000
cbcbcb
ffffff

Requirements
Must have
• Listed on the back, Earthworks | Haulage | Truck and Machinery Hire | Sand, Soil & Mulch Supply | Screening of Products
Nice to have
• Would be good for it to look appealing to a mans man, because it relates to heavy machinery, earthworks, construction etc. Black, red and white would be good maybe with a bit of silver somewhere.
Should not have
• not sure

```html
<!DOCTYPE html>
<html lang="en">
<head>
<meta charset="utf-8">
<title>Brolga Ridge Earthmoving &amp; Transport – Business Card</title>
<link href="https://fonts.googleapis.com/css2?family=Montserrat:ital,wght@0,600;0,700;0,800;1,600;1,700;1,800&display=swap" rel="stylesheet">
<style>
  :root {
    --red: #ec1f27;
    --black: #000000;
    --silver: #cbcbcb;
    --white: #ffffff;
    --backdrop: #370709;
    --ink: #111111;
  }
  * { margin: 0; padding: 0; box-sizing: border-box; }
  html, body { width: 1200px; height: 1000px; overflow: hidden; }
  body {
    background: var(--backdrop);
    font-family: "Montserrat", Arial, sans-serif;
    position: relative;
  }
  .card {
    position: absolute;
    left: 260px;
    width: 680px;
    height: 385px;
    border-radius: 24px;
    box-shadow: 0 8px 24px rgba(0,0,0,.45);
    overflow: hidden;
  }
  .card-front { top: 90px; background: var(--black); }
  .card-back {
    top: 515px;
    background: linear-gradient(180deg, #c9c9c9 0%, #efefef 55%, #dcdcdc 100%);
  }

  /* Brand lockup */
  .brand { position: absolute; display: flex; align-items: center; }
  .brand-square { background: var(--red); flex: none; }
  .brand-name {
    font-weight: 800;
    text-transform: uppercase;
    line-height: 1.08;
  }
  .card-front .brand {
    left: 0; right: 0; top: 150px; justify-content: center; gap: 22px;
  }
  .card-front .brand-square { width: 64px; height: 64px; }
  .card-front .brand-name { color: var(--white); font-size: 30px; }

  .card-back .brand { left: 36px; top: 80px; width: 262px; gap: 12px; }
  .card-back .brand-square { width: 40px; height: 40px; }
  .card-back .brand-name { color: var(--ink); font-size: 18px; }

  .divider {
    position: absolute; left: 312px; top: 42px;
    width: 3px; height: 164px; background: var(--ink);
  }

  .contact {
    position: absolute; left: 334px; top: 55px; width: 330px;
    color: var(--ink); white-space: nowrap;
  }
  .contact-name { font-weight: 800; font-size: 24px; letter-spacing: .3px; }
  .contact-role {
    color: var(--red); font-style: italic; font-weight: 700; font-size: 16px;
    margin-top: 2px;
  }
  .contact-line {
    display: flex; align-items: center; gap: 7px;
    font-weight: 700; font-size: 16px; margin-top: 8px;
  }
  .contact-line:first-of-type { margin-top: 16px; }
  .contact-line.email { font-size: 14px; letter-spacing: -.1px; }
  .contact-line svg { width: 15px; height: 17px; flex: none; }
  .contact-abn { font-weight: 700; font-size: 16px; margin-top: 14px; }

  .services { position: absolute; left: 12px; right: 12px; top: 237px; }
  .services-heading {
    background: var(--red); height: 38px; border-radius: 10px 10px 0 0;
    display: flex; align-items: center; justify-content: center;
    font-weight: 800; font-size: 19px; letter-spacing: 4px; color: var(--black);
  }
  .services-list {
    background: var(--black); height: 98px; border-radius: 0 0 10px 10px;
    display: flex; flex-direction: column; justify-content: center; gap: 8px;
    list-style: none;
  }
  .services-row { display: flex; justify-content: center; gap: 8px; }
  .service {
    display: flex; align-items: center; gap: 6px;
    color: var(--silver); font-style: italic; font-weight: 700; font-size: 19px;
  }
  .service svg { width: 26px; height: 22px; flex: none; }
</style>
</head>
<body>

<section class="card card-front" aria-label="Card front">
  <div class="brand">
    <span class="brand-square"></span>
    <span class="brand-name">Brolga Ridge<br>Earthmoving &amp; Transport</span>
  </div>
</section>

<section class="card card-back" aria-label="Card back">
  <div class="brand">
    <span class="brand-square"></span>
    <span class="brand-name">Brolga Ridge<br>Earthmoving &amp;<br>Transport</span>
  </div>

  <div class="divider"></div>

  <div class="contact">
    <p class="contact-name">DALE PETTIGREW</p>
    <p class="contact-role">Managing Director</p>
    <p class="contact-line">
      <svg viewBox="0 0 15 17"><rect x="2.5" y="1" width="10" height="15" rx="2" fill="none" stroke="#ec1f27" stroke-width="2"/><circle cx="7.5" cy="13" r="1" fill="#ec1f27"/></svg>
      0438 256 904
    </p>
    <p class="contact-line email">
      <svg viewBox="0 0 15 17"><rect x="0.5" y="3.5" width="14" height="10" fill="#ec1f27"/><path d="M1 4 L7.5 9.5 L14 4" fill="none" stroke="#fff" stroke-width="1.3"/></svg>
      brgtransport2011@haulmail.example
    </p>
    <p class="contact-abn">ABN 52 907 338 214</p>
  </div>

  <div class="services">
    <h2 class="services-heading">OUR SERVICES</h2>
    <ul class="services-list">
      <li class="services-row">
        <span class="service">Earthworks <svg viewBox="0 0 26 22"><path d="M2 12 L9 19 L24 3" fill="none" stroke="#ec1f27" stroke-width="4" stroke-linecap="round"/></svg></span>
        <span class="service">Haulage <svg viewBox="0 0 26 22"><path d="M2 12 L9 19 L24 3" fill="none" stroke="#ec1f27" stroke-width="4" stroke-linecap="round"/></svg></span>
        <span class="service">Truck and Machinery Hire <svg viewBox="0 0 26 22"><path d="M2 12 L9 19 L24 3" fill="none" stroke="#ec1f27" stroke-width="4" stroke-linecap="round"/></svg></span>
      </li>
      <li class="services-row">
        <span class="service">Sand, Soil &amp; Mulch Supply <svg viewBox="0 0 26 22"><path d="M2 12 L9 19 L24 3" fill="none" stroke="#ec1f27" stroke-width="4" stroke-linecap="round"/></svg></span>
        <span class="service">Screening of Products <svg viewBox="0 0 26 22"><path d="M2 12 L9 19 L24 3" fill="none" stroke="#ec1f27" stroke-width="4" stroke-linecap="round"/></svg></span>
      </li>
    </ul>
  </div>
</section>

</body>
</html>
```